DLM #4319 - Homepage Design

Theme: Sophisticated yet sporty and easy to navigate
Accent Color: Green to match the logo - if something else looks better with the design, then go for it.
Background: A curvy road possibly with a high end Italian car on it or a race track
Content Background: Can't exceed 950 pix wide. If there is an image in the background, then it may be best to make it somewhat transparent so you can see the image.

Banner:
Phone: 214-555-0193
Address: 4817 Pelham Ct. #200
Carrollton, TX 75099
Include social buttons in the banner: Facebook, Twitter, Youtube, Blog & eBay

Find 8 images of high end Italian vehicles & Valtrenne and use it in a slideshow
The images will include text such as: 'Buy with Confidence'

Include a space for a video as well

Make sure it says somewhere on the homepage: 'Been in business since 2004'

Large call to Action Buttons:
- Inventory
- Service
- Project Cars
- Contact Us

Requirements
Nice to have
• Dark background, but it may not work with the logo. If possible they would prefer a dark background.
Should not have
• No city backgrounds

```html
<!DOCTYPE html>
<html lang="en">
<head>
<meta charset="utf-8">
<title>DLM Performance – Home</title>
<link rel="stylesheet" href="https://fonts.googleapis.com/css2?family=Ubuntu:wght@400;500;700&family=Open+Sans:wght@400;600&display=swap">
<style>
:root{
  --green:#1a8a37;
  --green-dark:#0f6e2a;
  --green-light:#2aa548;
  --orange:#ff9a00;
  --orange-dark:#f07d00;
  --ink:#111;
  --text:#333;
  --muted:#777;
  --panel:#ffffff;
  --line:#d9d9d9;
}
*{box-sizing:border-box;margin:0;padding:0}
html,body{width:1136px;height:1200px;overflow:hidden}
body{position:relative;font-family:"Open Sans",sans-serif;color:var(--text);
  background:linear-gradient(180deg,#7fa2c4 0%,#c9d8e6 22%,#8fa38a 40%,#5d6a72 52%,#e6e9ec 66%,#ffffff 100%)}
a{text-decoration:none}
.backdrop{position:absolute;inset:0 0 auto 0;height:680px;
  background:linear-gradient(180deg,#6f96bd 0%,#c8d6e4 30%,#7e9c6a 46%,#4e5a63 60%,rgba(255,255,255,0) 100%)}
.page{position:absolute;left:126px;top:0;width:881px;height:1200px;background:rgba(255,255,255,.93)}
.header{position:absolute;left:0;top:0;width:881px;height:103px;
  background:linear-gradient(180deg,rgba(235,240,246,.9),rgba(255,255,255,.85))}
.logo{position:absolute;left:21px;top:18px;display:flex;align-items:center;gap:10px}
.logo-mark{width:38px;height:38px;background:var(--green)}
.logo-name{font-family:"Ubuntu",sans-serif;font-weight:700;font-size:34px;color:var(--green);letter-spacing:.5px}
.since{position:absolute;left:21px;top:71px;font-family:"Ubuntu",sans-serif;font-size:11.5px;font-weight:500;color:#222}
.follow{position:absolute;right:20px;top:12px;display:flex;align-items:center;gap:4px;font-size:11.5px;color:#444}
.follow span{margin-right:3px}
.social{width:26px;height:26px;border-radius:50%;display:block}
.s1{background:#3b5b9a}.s2{background:#38a1d8}.s3{background:#1d86c4}.s4{background:#d62d20}.s5{background:#f39c12}.s6{background:#111}
.help{position:absolute;right:21px;top:47px;font-size:11.5px;color:#444}
.call{position:absolute;right:22px;top:62px;font-family:"Ubuntu",sans-serif;font-weight:500;font-size:25px;color:#000}
.nav{position:absolute;left:0;top:103px;width:881px;height:40px;
  background:linear-gradient(180deg,var(--green-light),var(--green-dark));display:flex}
.nav a{display:block;height:40px;line-height:40px;padding:0 11px;font-family:"Ubuntu",sans-serif;font-weight:500;
  font-size:14.5px;color:#fff;border-right:1px solid rgba(0,0,0,.18)}
.nav a.active{background:linear-gradient(180deg,#ffb000,var(--orange-dark));padding:0 17px}
.nav a:last-child{border-right:0}
.hero{position:absolute;left:0;top:143px;width:881px;height:352px;
  background:linear-gradient(160deg,#9fb3c4 0%,#b9c6d1 30%,#2b4fb5 55%,#1b2f7a 72%,#6d7378 88%,#8a9095 100%)}
.hero-title{position:absolute;left:0;top:148px;width:227px;height:41px;background:var(--orange);
  font-family:"Ubuntu",sans-serif;font-size:20px;font-weight:500;color:#fff;line-height:41px;padding-left:20px}
.hero-cta{position:absolute;left:0;top:189px;width:109px;height:41px;background:#ffa31a;
  color:#fff;font-family:"Ubuntu",sans-serif;font-size:15px;line-height:41px;padding-left:21px}
.thumbs{position:absolute;left:287px;top:287px;display:flex;gap:6px}
.thumb{width:60px;height:47px;border:2px solid #fff}
.t1{background:linear-gradient(135deg,#c9d8a0,#6d9a2e)}
.t2{background:linear-gradient(135deg,#f4c400,#d07c00)}
.t3{background:linear-gradient(135deg,#f03a2a,#8a1008)}
.t4{background:linear-gradient(135deg,#ea4a3c,#a11c14)}
.t5{background:linear-gradient(135deg,#3b4c66,#10182a)}
.arrow{position:absolute;top:304px;width:18px;height:18px;border-radius:50%;background:var(--orange)}
.arrow svg{display:block}
.card{position:absolute;top:516px;width:263px;height:226px;background:var(--panel);
  box-shadow:0 1px 3px rgba(0,0,0,.25);padding:16px 14px 16px 19px}
.card h2{font-family:"Ubuntu",sans-serif;font-weight:500;font-size:20px;color:var(--ink);margin-bottom:5px}
.card p{font-size:12.6px;line-height:19.2px;color:#333;margin-bottom:4px;letter-spacing:-.1px}
.btn{display:inline-block;background:linear-gradient(180deg,var(--green-light),var(--green-dark));color:#fff;
  font-family:"Ubuntu",sans-serif;font-weight:500;font-size:13px;line-height:16px;padding:5px 13px;border-radius:3px;
  position:absolute;left:21px;bottom:12px;text-decoration:none}
.project{display:flex;gap:9px;margin-bottom:14px}
.project .pic{width:90px;height:58px;flex:none;margin-top:2px}
.project p{margin:0;line-height:19.4px;font-size:12.5px;white-space:nowrap}
.video{position:absolute;left:21px;top:760px;width:552px;height:298px;
  background:linear-gradient(180deg,#55677f 0%,#7d8fa6 40%,#7b94c9 60%,#3b3d42 85%,#2a2b2e 100%)}
.play{position:absolute;left:247px;top:112px}
.controls{position:absolute;left:0;bottom:0;width:552px;height:24px;background:#1f1f1f;display:flex;align-items:center}
.ctrl-btn{width:34px;height:24px;background:var(--green);display:flex;align-items:center;justify-content:center}
.track{flex:1;height:8px;margin:0 16px;background:#fff;position:relative}
.track::before{content:"";position:absolute;left:0;top:0;width:44px;height:8px;background:#aaa}
.enquire{position:absolute;left:599px;top:760px;width:263px;height:298px;background:var(--panel);
  border:1px solid var(--line);padding:16px 19px}
.enquire h2{font-family:"Ubuntu",sans-serif;font-weight:500;font-size:20px;color:var(--ink);margin-bottom:14px}
.field{height:31px;border:1px solid var(--line);font-size:12px;color:#666;padding:0 14px;line-height:29px;margin:0 2px 9px 2px}
.field.query{height:108px;line-height:normal;padding-top:13px;position:relative}
.go{position:absolute;right:12px;top:31px;width:48px;height:48px;border-radius:50%;
  background:radial-gradient(circle at 40% 35%,#ffc233,var(--orange-dark));color:#fff;font-family:"Ubuntu",sans-serif;
  font-size:18px;font-weight:500;text-align:center;line-height:48px}
.footer{position:absolute;left:0;top:1076px;width:881px;height:124px;
  background:linear-gradient(180deg,var(--green-light),var(--green-dark));color:#fff;text-align:center}
.footer-links{margin-top:22px;font-size:12.5px}
.footer-links a{color:#fff}
.footer-links i{font-style:normal;margin:0 8px}
.copy{font-size:12.5px;margin-top:8px}
.footer-social{display:flex;justify-content:center;gap:4px;margin-top:12px}
.footer-social span{width:26px;height:26px;border-radius:50%;background:#fff;display:block}
</style>
</head>
<body>
<div class="backdrop" role="img" aria-label="Open road through greenery under a bright sky"></div>
<div class="page">
  <header class="header">
    <div class="logo"><span class="logo-mark"></span><span class="logo-name">DLM Performance</span></div>
    <div class="since">Been in business since 2004</div>
    <div class="follow"><span>Follow Us</span>
      <a class="social s1" aria-label="Social link 1"></a><a class="social s2" aria-label="Social link 2"></a>
      <a class="social s3" aria-label="Social link 3"></a><a class="social s4" aria-label="Video channel"></a>
      <a class="social s5" aria-label="Blog feed"></a><a class="social s6" aria-label="Online store"></a>
    </div>
    <div class="help">We Can Help You, If You Have Any Questions</div>
    <div class="call">CALL US: 214-555-0193</div>
  </header>
  <nav class="nav">
    <a class="active" href="#">HOME</a><a href="#">ABOUT US</a><a href="#">INVENTORY</a>
    <a href="#">OUR SERVICES</a><a href="#">PROJECT CARS</a><a href="#">CONTACT US</a>
  </nav>
  <section class="hero" role="img" aria-label="Blue Italian sports coupe driving at speed">
    <div class="hero-title">Buy with Confidence</div>
    <div class="hero-cta">Click Here</div>
    <div class="arrow" style="left:270px"><svg width="18" height="18"><path d="M11 5 L6 9 L11 13Z" fill="#fff"/></svg></div>
    <div class="thumbs">
      <div class="thumb t1" role="img" aria-label="Green sports car"></div>
      <div class="thumb t2" role="img" aria-label="Yellow sports car"></div>
      <div class="thumb t3" role="img" aria-label="Red sports car"></div>
      <div class="thumb t4" role="img" aria-label="Red coupe"></div>
      <div class="thumb t5" role="img" aria-label="Dark blue coupe"></div>
    </div>
    <div class="arrow" style="left:627px"><svg width="18" height="18"><path d="M7 5 L12 9 L7 13Z" fill="#fff"/></svg></div>
  </section>

  <article class="card" style="left:21px">
    <h2>Inventory</h2>
    <p>Looking for a specific new car, or<br>SUV from a local dealer?</p>
    <p>Lorem Ipsum is simply dummy text of<br>the printing and typesetting industry.<br>Lorem Ipsum has been the industry's<br>standard dummy text ever<br>since the 1500s</p>
    <a class="btn" href="#">Know More</a>
  </article>
  <article class="card" style="left:310px">
    <h2>Our Services</h2>
    <p>Looking for a specific new car, or<br>SUV from a local dealer?</p>
    <p>Lorem Ipsum is simply dummy text of<br>the printing and typesetting industry.<br>Lorem Ipsum has been the industry's<br>standard dummy text ever<br>since the 1500s</p>
    <a class="btn" href="#">Know More</a>
  </article>
  <article class="card" style="left:599px">
    <h2>Project Cars</h2>
    <div class="project"><div class="pic" role="img" aria-label="Red striped sports car" style="background:linear-gradient(135deg,#8fa0b3,#c8202a 55%,#3a3a3a)"></div><p>Lorem Ipsum is simply<br>dummy text of the<br>printing &amp; typesetting</p></div>
    <div class="project"><div class="pic" role="img" aria-label="Blue sports car" style="background:linear-gradient(135deg,#b7c7d8,#1e4fd0 55%,#444)"></div><p>Lorem Ipsum is simply<br>dummy text of the<br>printing &amp; typesetting</p></div>
    <a class="btn" href="#">Know More</a>
  </article>

  <section class="video" role="img" aria-label="Video of a blue and white police sports car">
    <svg class="play" width="62" height="62"><circle cx="31" cy="31" r="28" fill="none" stroke="#ffb400" stroke-width="5"/><path d="M25 19 L43 31 L25 43Z" fill="#ffb400"/></svg>
    <div class="controls">
      <div class="ctrl-btn"><svg width="12" height="12"><path d="M2 1 L11 6 L2 11Z" fill="#fff"/></svg></div>
      <div class="track"></div>
      <div class="ctrl-btn"><svg width="16" height="12"><rect x="1" y="1" width="14" height="10" fill="none" stroke="#fff" stroke-width="1.5"/></svg></div>
    </div>
  </section>

  <section class="enquire">
    <h2>Enquire Now</h2>
    <div class="field">Your Name</div>
    <div class="field">Phone Number</div>
    <div class="field">Email Address</div>
    <div class="field query">Query<div class="go">GO</div></div>
  </section>

  <footer class="footer">
    <div class="footer-links"><a href="#">Home</a><i>|</i><a href="#">About Us</a><i>|</i><a href="#">Services</a><i>|</i><a href="#">Project Cars</a><i>|</i><a href="#">Contact Us</a></div>
    <div class="copy">Copyright © 2014 DLM. All Rights Reserved.</div>
    <div class="footer-social"><span></span><span></span><span></span><span></span><span></span><span></span></div>
  </footer>
</div>
</body>
</html>
```